Business Card Design Project

New Private residential substance abuse treatment facility in Mapleton, UT. Facility located in elegant 11,000 home with stunning views of the mountains. Wish to incorporate colored logo. Business name- Cedar Brook Wellness. Facility is Tudor style with traditional furnishings, an overhead picture is attached. Lettering in a simple scroll or old english style. Must be easy to read with clear moderetly large font.
Updates

It seems the project time frame listed was not correct- it is a week.

Target Market(s)

Adults 18 and over with substance abuse issues requiring residential rehabilitation. Referral base are medical/mental health professionals, families and community agencies.

Industry/Entity Type

Residential

Colors
9bcb3b
fece3e
fbee3f

Requirements
Must have
• Clear and easy to read, professional and upscale presentation. Need logo, name, title, address, phone, fax and web page address. May add slogan later. Use same font as logo.
Nice to have
• Logo has a green mountain and a gold maple leaf so a nature themed element may work. Want to promote peaceful grounded image. Logo attached.
Should not have
• No tiny or complicated font. No modern or tech looking images. No light colored fonts.

```html
<!DOCTYPE html>
<html lang="en">
<head>
<meta charset="UTF-8">
<title>Cedar Brook Wellness – Business Card</title>
<link rel="stylesheet" href="https://fonts.googleapis.com/css2?family=Lato:wght@400&display=swap">
<style>
  :root {
    --card-green: #9bcb3b;
    --icon-gold: #fece3e;
    --ink: #3b3b3f;
    --rule-dark: #4f6a1c;
  }
  html, body {
    margin: 0;
    padding: 0;
    width: 1200px;
    height: 720px;
    overflow: hidden;
  }
  .card {
    position: relative;
    width: 1200px;
    height: 720px;
    background: var(--card-green);
    font-family: "Lato", sans-serif;
    color: var(--ink);
  }
  .brand-name {
    position: absolute;
    left: 97px;
    top: 318px;
    width: 412px;
    margin: 0;
    text-align: center;
    font-size: 37px;
    font-weight: 400;
    letter-spacing: 1px;
    color: var(--ink);
  }
  .contact-rule {
    position: absolute;
    left: 664px;
    top: 209px;
    width: 1px;
    height: 274px;
    background: linear-gradient(to bottom, rgba(79,106,28,0) 0%, var(--rule-dark) 50%, rgba(79,106,28,0) 100%);
  }
  .contact-list {
    position: absolute;
    left: 598px;
    top: 0;
    margin: 0;
    padding: 0;
    list-style: none;
  }
  .contact-item {
    position: absolute;
    left: 0;
    display: flex;
    align-items: center;
    white-space: nowrap;
    transform: translateY(-50%);
  }
  .contact-icon {
    width: 38px;
    height: 34px;
    fill: var(--icon-gold);
  }
  .contact-text {
    margin-left: 50px;
    font-size: 25px;
    letter-spacing: 2.4px;
  }
  .contact-text.is-heading {
    font-size: 28px;
    letter-spacing: 3px;
  }
</style>
</head>
<body>
<main class="card">
  <h1 class="brand-name">Cedar Brook Wellness</h1>

  <div class="contact-rule"></div>

  <ul class="contact-list">
    <li class="contact-item" style="top:232px">
      <svg class="contact-icon" viewBox="0 0 38 34" aria-hidden="true">
        <path d="M19 3 L3 17 H8 V31 H16 V22 H22 V31 H30 V17 H35 Z"/>
      </svg>
      <span class="contact-text is-heading">ADRESS</span>
    </li>
    <li class="contact-item" style="top:278px">
      <svg class="contact-icon" viewBox="0 0 38 34" aria-hidden="true">
        <path d="M13 1 H25 A3 3 0 0 1 28 4 V30 A3 3 0 0 1 25 33 H13 A3 3 0 0 1 10 30 V4 A3 3 0 0 1 13 1 Z M12.5 5 V26 H25.5 V5 Z M19 27.5 A1.5 1.5 0 1 0 19 30.5 A1.5 1.5 0 1 0 19 27.5 Z" fill-rule="evenodd"/>
      </svg>
      <span class="contact-text">012-345-678</span>
    </li>
    <li class="contact-item" style="top:329px">
      <svg class="contact-icon" viewBox="0 0 38 34" aria-hidden="true">
        <path d="M9 3 L14 2 L18 10 L14 13 C16 18 19 21 24 23 L27 19 L35 23 L34 28 C33 31 30 32 27 31 C17 28 10 21 7 11 C6 8 7 5 9 3 Z"/>
      </svg>
      <span class="contact-text">012-345-678</span>
    </li>
    <li class="contact-item" style="top:376px">
      <svg class="contact-icon" viewBox="0 0 38 34" aria-hidden="true">
        <path d="M11 2 H27 V10 H11 Z M6 12 H32 A3 3 0 0 1 35 15 V25 H29 V21 H9 V25 H3 V15 A3 3 0 0 1 6 12 Z M11 23 H27 V32 H11 Z M14 26 V29 H24 V26 Z" fill-rule="evenodd"/>
      </svg>
      <span class="contact-text">012-345-678</span>
    </li>
    <li class="contact-item" style="top:421px">
      <svg class="contact-icon" viewBox="0 0 38 34" aria-hidden="true">
        <path d="M22 28 C12 32 4 26 4 18 C4 9 11 3 19 3 C27 3 33 8 33 16 C33 22 30 25 27 25 C24 25 23 23 23 21 C21 24 19 25 16 24 C13 23 12 20 13 16 C14 11 19 9 23 11 L24 10 H27 L26 20 C26 21.5 27 22 28 21.5 C29.5 20.5 30 18.5 30 16 C30 10 25 6 19 6 C13 6 7 10 7 18 C7 25 14 29 21 25.5 Z M17 17 C16.5 19.5 17.5 21 19.5 20.5 C21.5 20 22.5 18 22.8 15 C22 13.5 21 13 19.8 13.2 C18.3 13.5 17.4 15 17 17 Z" fill-rule="evenodd"/>
      </svg>
      <span class="contact-text">EMAIL@SITE.COM</span>
    </li>
    <li class="contact-item" style="top:464px">
      <svg class="contact-icon" viewBox="0 0 38 34" aria-hidden="true" fill="none" stroke="#fece3e" stroke-width="2.6">
        <circle cx="19" cy="17" r="14"/>
        <ellipse cx="19" cy="17" rx="6" ry="14"/>
        <line x1="5" y1="17" x2="33" y2="17"/>
        <path d="M8 9 H30 M8 25 H30"/>
      </svg>
      <span class="contact-text">WEBSITE.COM</span>
    </li>
  </ul>
</main>
</body>
</html>
```